Kavoni. Sunless Tanning Mousse Label

I'm looking for a label creation for a new brand of sunless tanning solutions. They are in 6.7oz bottles (template attached).

For the front of the bottle (see template) I would like an abstract multi coloured design taking up just over half the top of the bottle (approx 60%) and going around the design (this is similar to the design inspiration attached). I would this design to use the attached colour palette of pinks. It can be swirls, drips, squares, lines, whatever you think will look good.

The logo will then be over top of that abstract design in the upper 1/3, in the colour #3fe0d0

Under the abstract design the following text:

Wild Plume (Larger text)
Coral Drift (2nd heading)
1 Hour Sunless Mousse (Sub text)
The No Orange Guarantee! (Sub text)
Vegan Formula (sub text)

The sub texts for above can be fun, have coloured background, different fonts, whatever looks good and is sill fun.

Towards the bottom of the front of bottle we require the sizing information:

200ml 6.7 Fl Oz

On the left side of the front (so in the template the middle smaller section) I would like the phrase "You ain't gotta get ready if you stay ready" Could you please make this as a separate little quote, with a fun design to it. It's like a little hidden gem on the side of the bottle.

On the back of the bottle for now can you please start towards the top with:

Wild Plume Mousse (larger)
Coral drift (second heading)
Deep Mediterranean Inspired Tan (second heading)
Easy to Apply & Streak Free
Vegan friendly & 100% natural DHA tan actives

Under this I require approx 1.5" of Lorem Ipsum for now which will take the place of directions for using the product.

Under that in small writing can we include "Warning: This product does not contain a sunscreen and will not protect against sunburn. For external use only. If skin irritation occurs, discontinue use. Carry out a patch test 24 hours prior to full body use. Store below 25(degrees sign)C."

At the bottom is the smallest yet still legible writing, can we include the ingredients that are listed below.

Target Market(s)

Females 24-35 who take care of themselves and always want to look good. It's a youthful fun product.

Requirements
Must have
• Bright colours, and just screams FUN and youthful.

Ingredients must be listed on the back. They dont' need to take up more than an inch in height, less if possible.
*******************************************

INGREDIENTS: Water (Aqua), Propylene Glycol, Dihydroxyacetone, Peg-6 Caprylic/Capric Glycerides, Dihydroxypropyl Peg-5 Linoleammonium Chloride, Peg-7 Glyceryl Cocoate, Caramel,
Phenoxyethanol, Caprylyl Glycol, Potassium Sorbate, Hexylene Glycol, Glycerin, Helianthus Annuus (Sunflower) Seed Oil, Beta Vulgaris (Beet) Root Extract, Panthenol, Solanum Lycopersicum
(Tomato) Fruit Extract, Vaccinium Macrocarpon (Cranberry) Fruit Extract, L-ascorbic Acid (Vitamin C), Tocopheryl Acetate (Vitamin E), Theobroma Cacao (Cocoa) Seed Butter, Rosa Canina (Rose Hip)
Fruit Oil, Glycine Soja (Soybean) Oil, Cucumis Sativus (Cucumber) Fruit Extract, Blue 1 (CI 42090), Red 40 (CI 16035), Yellow 6 (CI 15985), Green 5 (CI 61570), Yellow 5 (CI 19140), Red 33 (CI 17200)

*****************************
Nice to have
• Several options to choose from, some can include a gradient into geometric shapes, rather than solid colour. Experiment
Should not have
• Do not want it to look medical.
Want colours to stay in the same pink family for the abstract design - can use white also.

```html
<!DOCTYPE html>
<html lang="en">
<head>
<meta charset="utf-8">
<title>Kavoni – Wild Plume Sunless Mousse Label</title>
<link rel="stylesheet" href="https://fonts.googleapis.com/css2?family=Questrial&family=Cormorant+SC:wght@500&family=Caveat:wght@500&display=swap">
<style>
  :root {
    --page-bg: #ffffff;
    --label-white: #ececec;
    --pink-deep: #c8566a;
    --pink-mid: #dc8a98;
    --pink-soft: #efc4cc;
    --ink: #3a3a3a;
    --ink-soft: #555555;
    --pill: #d93f7f;
    --logo: #ffffff;
  }
  * { margin: 0; padding: 0; box-sizing: border-box; }
  html, body {
    width: 740px;
    height: 1200px;
    overflow: hidden;
    background: var(--page-bg);
  }
  .label {
    position: absolute;
    left: 190px;
    top: 40px;
    width: 360px;
    height: 1120px;
    background: var(--label-white);
    overflow: hidden;
  }
  .label__art {
    position: absolute;
    inset: 0;
    width: 100%;
    height: 100%;
  }
  .brand {
    position: absolute;
    top: 330px;
    left: 70px;
    font-family: "Questrial", sans-serif;
    font-size: 40px;
    letter-spacing: 2px;
    color: var(--logo);
  }
  .product-info {
    position: absolute;
    top: 752px;
    left: 0;
    width: 100%;
    text-align: center;
    color: var(--ink);
  }
  .product-name {
    font-family: "Questrial", sans-serif;
    font-size: 48px;
    line-height: 1;
    letter-spacing: 0.5px;
  }
  .product-variant {
    margin-top: 4px;
    font-family: "Cormorant SC", serif;
    font-size: 24px;
    color: var(--ink-soft);
  }
  .pill {
    display: inline-block;
    margin-top: 6px;
    padding: 3px 14px 4px;
    border-radius: 12px;
    background: var(--pill);
    color: #fff;
    font-family: "Questrial", sans-serif;
    font-size: 17px;
  }
  .guarantee {
    margin-top: 4px;
    font-family: "Caveat", cursive;
    font-size: 26px;
    color: var(--ink);
    transform: rotate(-3deg);
  }
  .vegan {
    margin-top: 2px;
    font-family: "Cormorant SC", serif;
    font-size: 20px;
    color: var(--ink-soft);
  }
  .size {
    position: absolute;
    top: 1010px;
    width: 100%;
    text-align: center;
    font-family: "Cormorant SC", serif;
    font-size: 14px;
    color: var(--ink-soft);
  }
</style>
</head>
<body>
  <main class="label">
    <svg class="label__art" viewBox="0 0 360 1120" preserveAspectRatio="none" role="img" aria-label="Abstract pink swirl pattern sweeping across the upper label">
      <defs>
        <linearGradient id="swirl" x1="0" y1="0" x2="1" y2="1">
          <stop offset="0" stop-color="#e6a9b3"/>
          <stop offset="0.4" stop-color="#c8566a"/>
          <stop offset="0.7" stop-color="#dc8a98"/>
          <stop offset="1" stop-color="#efc4cc"/>
        </linearGradient>
      </defs>
      <path d="M0 0 H360 V560 C250 640 110 780 40 1120 H0 Z" fill="url(#swirl)"/>
    </svg>

    <div class="brand">Kavoni</div>

    <section class="product-info">
      <h1 class="product-name">Wild Plume</h1>
      <p class="product-variant">Coral Drift</p>
      <span class="pill">1 Hour Sunless Mousse</span>
      <p class="guarantee">The No Orange Guarantee!</p>
      <p class="vegan">Vegan Formula</p>
    </section>

    <p class="size">200ml 6.7 Fl Oz</p>
  </main>
</body>
</html>
```